Business Card Design Project

We need a new business card design to go along with the look of our new website. tolvarex.com We manufacture after market woodworking machinery parts. Please take a look at the colors on our website and use the same.

Industry/Entity Type

Woodworking

```html
<!DOCTYPE html>
<html lang="en">
<head>
<meta charset="utf-8">
<title>Tolvarex Business Card</title>
<link href="https://fonts.googleapis.com/css2?family=Source+Sans+3:wght@400;600;700&display=swap" rel="stylesheet">
<style>
  :root {
    --stage: #555657;
    --card: #efefef;
    --green: #1f8a3c;
    --green-deep: #16772f;
    --ink: #2b2b2b;
    --white: #ffffff;
  }
  html, body {
    margin: 0;
    padding: 0;
    width: 1200px;
    height: 900px;
    overflow: hidden;
    background: var(--stage);
    font-family: "Source Sans 3", Arial, sans-serif;
  }
  .card {
    position: absolute;
    top: 300px;
    width: 525px;
    height: 300px;
    border-radius: 14px;
    background: var(--card);
    overflow: hidden;
  }
  .card-front { left: 58px; }
  .card-back { left: 617px; }
  .card svg.decor {
    position: absolute;
    inset: 0;
    width: 525px;
    height: 300px;
  }
  .brand-front {
    position: absolute;
    left: 30px;
    top: 118px;
    display: flex;
    align-items: center;
    gap: 14px;
    font-weight: 700;
    font-size: 52px;
    letter-spacing: 1px;
    color: var(--green);
  }
  .brand-dot {
    width: 26px;
    height: 26px;
    border-radius: 50%;
    background: var(--green);
  }
  .contact {
    position: absolute;
    left: 41px;
    top: 48px;
    color: var(--ink);
    font-size: 13.5px;
    line-height: 17px;
  }
  .contact .name {
    font-size: 17px;
    font-weight: 700;
    color: var(--green);
    letter-spacing: 0.5px;
  }
  .contact .role {
    font-size: 13.5px;
    color: var(--ink);
    font-weight: 400;
  }
  .contact .company {
    margin-top: 14px;
    font-size: 15px;
    color: var(--green);
  }
  .contact .lines { margin-top: 2px; }
  .contact .phones { margin-top: 14px; }
  .contact .label { color: var(--green); }
  .brand-back {
    position: absolute;
    right: 44px;
    top: 112px;
    width: 230px;
    text-align: center;
    font-weight: 700;
    font-size: 18px;
    line-height: 21px;
    color: var(--green);
  }
  .web {
    position: absolute;
    right: 27px;
    bottom: 22px;
    color: var(--white);
    font-weight: 700;
    font-size: 16px;
    letter-spacing: 0.3px;
  }
</style>
</head>
<body>
  <section class="card card-front">
    <svg class="decor" viewBox="0 0 525 300" aria-hidden="true">
      <path d="M0 0 H330 C410 10 460 35 440 50 C360 28 220 28 120 40 C70 46 30 52 0 60 Z" fill="var(--green)"/>
      <path d="M330 0 H360 C470 30 540 90 525 150 L525 205 C510 150 470 70 330 0 Z" fill="var(--green-deep)"/>
      <path d="M0 295 C170 290 380 260 525 180 L525 192 C380 272 170 300 0 300 Z" fill="var(--green)"/>
      <path d="M0 248 C40 252 90 262 130 276 C80 276 40 274 0 272 Z" fill="var(--green)"/>
    </svg>
    <div class="brand-front"><span class="brand-dot"></span>TOLVAREX</div>
  </section>

  <section class="card card-back">
    <svg class="decor" viewBox="0 0 525 300" aria-hidden="true">
      <path d="M0 268 C120 262 280 240 400 218 C450 210 490 214 525 214 V300 H0 Z" fill="var(--green)"/>
      <path d="M0 254 C160 258 330 230 480 210 C440 222 280 250 0 262 Z" fill="var(--green)"/>
    </svg>
    <div class="contact">
      <div><span class="name">MARLOW KEEN</span> <span class="name">:</span> <span class="role">Manager</span></div>
      <div class="company">Tolvarex Machine Parts</div>
      <div class="lines">2280 Alder Ridge Road #312<br>Fernvale CA 90412 USA</div>
      <div class="phones">
        <span class="label">Toll Free :</span> 877.555.0148<br>
        <span class="label">Phone :</span> 909.555.0172<br>
        <span class="label">Fax :</span> 909.555.0193<br>
        <span class="label">Email :</span> Sales@Tolvarex.com
      </div>
    </div>
    <div class="brand-back">TOLVAREX MACHINE PARTS INC.</div>
    <div class="web">www.tolvarex.com</div>
  </section>
</body>
</html>
```